Business Card for staff member of football club SC Brenval

I would like to get a business card template for all staff member of our soccer club.

The card should use as much as possible the 2 colors of the club : Red which is the main color and blue which is the alternative color. It can be balanced between the two like our logo.

I prefer simple and lean design.

Contact Information for Business Card

Bussiness card should have all main stuff as describe here below in must have.

Font styles to use
Sans Serif

Requirements
Must have
• Name : Laurent DESPRATIN
Fonction : Président
Mobile : +41 xx xxx xx xx
Email : first.lastname@scbrenval.ch
Adresse of the club : SC Brenval, 1873 Brenval
Website of the club : www.scbrenval.ch
Nice to have
• Version with and without picture of the staff member

A version for men, a version for women staff member.

```html
<!DOCTYPE html>
<html lang="fr">
<head>
<meta charset="utf-8">
<title>SC Brenval – Carte de visite</title>
<link rel="stylesheet" href="https://fonts.googleapis.com/css2?family=Oswald:wght@500;600&family=Work+Sans:wght@400&display=swap">
<style>
  :root {
    --club-red: #e8213a;
    --club-blue: #0a86cc;
    --card-white: #ffffff;
    --ink: #1f1f1f;
    --backdrop: #4a3322;
  }
  * { margin: 0; padding: 0; box-sizing: border-box; }
  html, body { width: 1200px; height: 900px; overflow: hidden; }
  body { background: var(--backdrop); position: relative; font-family: "Work Sans", sans-serif; }

  .card { position: absolute; top: 230px; width: 347px; height: 440px; }
  .card-front { left: 218px; }
  .card-back { left: 637px; }
  .card-shape { position: absolute; inset: 0; width: 347px; height: 440px; filter: drop-shadow(0 3px 6px rgba(0,0,0,.35)); }

  .card-content { position: absolute; inset: 0; text-align: center; }
  .club-name {
    position: absolute; left: 0; right: 0; top: 50px;
    font-family: "Oswald", sans-serif; font-weight: 600; font-size: 54px; line-height: 1;
    color: var(--club-red); letter-spacing: 0.5px;
  }
  .staff-name {
    position: absolute; left: 0; right: 0; top: 158px;
    font-family: "Oswald", sans-serif; font-weight: 500; font-size: 26px; line-height: 1; letter-spacing: .5px;
  }
  .staff-name .first { color: var(--club-blue); }
  .staff-name .last { color: var(--club-red); }
  .staff-role { position: absolute; left: 0; right: 0; top: 190px; font-size: 16px; color: var(--ink); }
  .contact-icons { position: absolute; left: 0; right: 0; top: 224px; display: flex; justify-content: center; gap: 9px; }
  .contact-icons svg { width: 11px; height: 11px; }
  .contact-lines { position: absolute; left: 0; right: 0; top: 246px; font-size: 16px; line-height: 21px; color: var(--ink); }

  .back-name {
    position: absolute; left: 0; right: 0; top: 160px;
    font-family: "Oswald", sans-serif; font-weight: 600; font-size: 56px; line-height: 1;
    color: var(--card-white); text-align: center;
  }
</style>
</head>
<body>

<div class="card card-front">
  <svg class="card-shape" viewBox="0 0 347 440">
    <polygon points="0,0 347,0 347,318 173.5,440 0,318" fill="var(--card-white)"/>
    <polyline points="169,12 14,12 14,304 169,421" fill="none" stroke="var(--club-red)" stroke-width="6"/>
    <polyline points="178,12 333,12 333,304 178,421" fill="none" stroke="var(--club-blue)" stroke-width="6"/>
  </svg>
  <div class="card-content">
    <div class="club-name">SC Brenval</div>
    <div class="staff-name"><span class="first">LAURENT</span> <span class="last">DESPRATIN</span></div>
    <div class="staff-role">Président</div>
    <div class="contact-icons" aria-hidden="true">
      <svg viewBox="0 0 12 12"><path d="M3 1 L5 3.5 L4 4.8 Q5 7 7.2 8 L8.5 7 L11 9 L9.5 11 Q3 10 1 2.5 Z" fill="none" stroke="var(--club-red)" stroke-width="1.1"/></svg>
      <svg viewBox="0 0 12 12"><rect x="1" y="2.5" width="10" height="7" fill="none" stroke="var(--club-red)" stroke-width="1.1"/><polyline points="1,2.5 6,6.5 11,2.5" fill="none" stroke="var(--club-red)" stroke-width="1.1"/></svg>
      <svg viewBox="0 0 12 12"><circle cx="6" cy="6" r="5" fill="none" stroke="var(--club-red)" stroke-width="1"/><ellipse cx="6" cy="6" rx="2.2" ry="5" fill="none" stroke="var(--club-red)" stroke-width="1"/><line x1="1" y1="6" x2="11" y2="6" stroke="var(--club-red)" stroke-width="1"/></svg>
      <svg viewBox="0 0 12 12"><path d="M6 11.5 Q2 6.5 2 4.5 A4 4 0 0 1 10 4.5 Q10 6.5 6 11.5 Z" fill="var(--club-red)"/><circle cx="6" cy="4.5" r="1.4" fill="var(--card-white)"/></svg>
    </div>
    <div class="contact-lines">
      <div>+41 xx xxx xx xx</div>
      <div>first.lastname@scbrenval.ch</div>
      <div>www.scbrenval.ch</div>
      <div>SC Brenval, 1873 Brenval</div>
    </div>
  </div>
</div>

<div class="card card-back">
  <svg class="card-shape" viewBox="0 0 347 440">
    <polygon points="0,0 347,0 347,318 173.5,440 0,318" fill="var(--club-red)"/>
  </svg>
  <div class="back-name">SC Brenval</div>
</div>

</body>
</html>
```